Website for a start-up named Vlm Quarvex.

The company is currently producing a sustainable tactical training measure for soldiers in the defense industry. We’d like a simple website design. As the product hasn’t been launched yet, we will not tell too much about the product and it’s not for sale either. We have a website on wix called vlmquarvex.com which we would like to proceed with. The design just needs a professional and loving touch. We develop an add on for TK40 rifles.

Target Market(s)

Defense industry

Industry/Entity Type

Defense

Coding

Coded - Design and coding required

Number of Pages Required

1 page

```html
<!DOCTYPE html>
<html lang="en">
<head>
<meta charset="utf-8">
<title>Vlm Quarvex – Website Design</title>
<link href="https://fonts.googleapis.com/css2?family=Exo+2:wght@500;600;700&family=Roboto:wght@400;500;700&display=swap" rel="stylesheet">
<style>
:root{
  --teal:#00a79d;
  --ink:#3a3a3a;
  --text:#666;
  --soft:#f4f4f4;
  --field:#eeeeee;
  --footer:#555555;
  --stage:#e4e4e4;
  --white:#fff;
}
*{margin:0;padding:0;box-sizing:border-box}
html,body{width:991px;height:1200px;overflow:hidden;background:var(--stage)}
body{position:relative;font-family:"Roboto",Arial,sans-serif;color:var(--ink)}
.page{position:absolute;top:58px;width:427px;background:var(--white);overflow:hidden;box-shadow:0 1px 4px rgba(0,0,0,.12)}
.page-a{left:51px;height:945px}
.page-b{left:512px;height:1083px}
.abs{position:absolute}
.head-font{font-family:"Exo 2",Arial,sans-serif;font-weight:700;text-transform:uppercase;letter-spacing:.2px}
.teal{color:var(--teal)}
/* header */
.site-header{left:0;top:0;width:427px;height:32px;background:var(--white)}
.brand{font-family:"Roboto",Arial,sans-serif;font-weight:700;font-size:9px;color:var(--teal);display:flex;align-items:center;gap:3px;white-space:nowrap}
.brand-dot{width:6px;height:6px;border-radius:50%;background:var(--teal)}
.nav-link{top:12px;font-size:5.2px;font-weight:500;color:#222;white-space:nowrap}
.nav-link.active{color:var(--teal)}
.nav-link.active::after{content:"";position:absolute;left:-1px;right:-1px;top:8px;height:1px;background:var(--teal)}
.quote-btn{left:335px;top:9px;width:52px;height:14px;border-radius:8px;background:var(--teal);color:#fff;font-size:5.2px;font-weight:500;display:flex;align-items:center;justify-content:center}
/* photo fills */
.photo{position:absolute}
.hero-a{left:0;top:32px;width:427px;height:215px;background:linear-gradient(135deg,#7d7266 0%,#9a8f83 40%,#6e6a63 100%)}
.hero-b{left:0;top:32px;width:427px;height:240px}
.hero-title{font-size:18px;color:#fff;font-weight:600}
.hero-copy{font-size:5.6px;line-height:9px;color:#fff;width:150px}
.pill{border-radius:9px;background:var(--teal);color:#fff;font-weight:700;font-size:5.6px;display:flex;align-items:center;justify-content:center;gap:3px;text-transform:uppercase}
.pill i{width:5px;height:5px;border-radius:50%;background:#fff;display:inline-block;position:relative}
.pill i::after{content:"";position:absolute;left:1.5px;top:1.3px;border-left:2px solid var(--teal);border-top:1.2px solid transparent;border-bottom:1.2px solid transparent}
/* sections */
.sec-title{font-size:14px;line-height:16px;color:var(--ink)}
.sec-sub{font-size:5.6px;font-weight:700;color:#222}
.body-copy{font-size:4.6px;line-height:9.1px;color:var(--text)}
.soft-band{background:var(--soft)}
.big-brand{font-family:"Roboto",Arial,sans-serif;font-weight:700;font-size:28px;color:#333;display:flex;align-items:center;gap:8px;white-space:nowrap}
.big-brand .sq{width:16px;height:16px;background:#333}
/* testimonials */
.clients{left:0;width:427px;background:var(--teal);color:#fff}
.clients-title{font-size:12px;color:#fff;font-weight:600}
.avatar{width:33px;height:33px;transform:rotate(45deg);background:linear-gradient(135deg,#7fb6d8,#3e6f99);border-radius:3px}
.quote-text{font-size:5.2px;line-height:9.5px;font-style:italic;color:#fff;width:240px}
.quote-mark{font-family:Georgia,serif;font-size:16px;color:rgba(255,255,255,.35);line-height:1}
.client-name{font-size:5.6px;font-weight:500}
.client-co{font-size:4px}
.chev{width:9px;height:9px;border-left:1.6px solid #fff;border-bottom:1.6px solid #fff}
/* contact */
.contact-title{left:0;width:427px;text-align:center;font-size:16px;font-weight:600}
.col-title{font-size:7px;font-weight:500;color:#333}
.small-copy{font-size:4.8px;line-height:8px;color:#555}
.map{background:linear-gradient(135deg,#4d4d4d,#3a3a3a)}
.field{background:var(--field);border:1px solid #e2e2e2;font-size:4px;color:#777;padding:0 6px;display:flex;align-items:center}
.field.tall{align-items:flex-start;padding-top:12px}
.submit{background:var(--teal);color:#fff;font-size:5px;font-weight:700;display:flex;align-items:center;justify-content:center}
.icon{width:6px;height:6px}
/* footer */
.bar-footer{left:0;width:427px;height:18px;background:var(--footer);color:#fff;font-size:5.2px}
.ring{width:9px;height:9px;border:0.8px solid #fff;border-radius:50%}
.full-footer{left:0;top:955px;width:427px;height:128px;background:var(--footer);color:#fff}
.f-head{font-size:5.6px;font-weight:700}
.f-link{font-size:4.4px;line-height:9.2px;color:#eee}
.f-label{font-size:4px;font-weight:700}
.f-val{font-size:4.4px;line-height:6px}
</style>
</head>
<body>

<!-- ============ PAGE A ============ -->
<section class="page page-a">
  <header class="abs site-header">
    <div class="abs brand" style="left:40px;top:11px"><span class="brand-dot"></span>VLM QUARVEX</div>
    <span class="abs nav-link active" style="left:148px">Home</span>
    <span class="abs nav-link" style="left:174px">Who We Are</span>
    <span class="abs nav-link" style="left:215px">Services</span>
    <span class="abs nav-link" style="left:247px">Our Technology</span>
    <span class="abs nav-link" style="left:296px">Contact Us</span>
    <span class="abs quote-btn">Get A Quote</span>
  </header>

  <div class="photo hero-a" role="img" aria-label="Trainees in black practising pistol drills at an outdoor range with tyres and targets"></div>
  <h1 class="abs head-font hero-title" style="left:39px;top:98px">VLM QUARVEX</h1>
  <p class="abs hero-copy" style="left:40px;top:127px">Welcome to Vlm Quarvex, the advanced Technology Company paving the way to the future.</p>
  <span class="abs pill" style="left:40px;top:157px;width:68px;height:18px">Learn More <i></i></span>

  <div class="abs big-brand" style="left:34px;top:305px;font-size:24px"><span class="sq"></span>Vlm Quarvex</div>

  <h2 class="abs head-font sec-title" style="left:231px;top:279px">Who <span class="teal">We Are</span></h2>
  <p class="abs sec-sub" style="left:231px;top:297px">We develop an add on for TK40 rifles.</p>
  <p class="abs body-copy" style="left:231px;top:309px;width:158px">Vlm Quarvex is a leading provider of cutting-edge technologies and services, offering scalable solutions for the defense and security industry of all sizes. Founded by a group of friends who started by scribbling their ideas on a bus ride in San Francisco. Today we are working on innovative solutions to disrupt the training industry with a sustainable solution.</p>

  <div class="abs soft-band" style="left:0;top:406px;width:427px;height:186px"></div>
  <svg class="abs" style="left:0;top:406px" width="427" height="186" role="img" aria-label="Two soldiers aiming rifles on a green shooting range">
    <defs><linearGradient id="gA" x1="0" y1="0" x2="0" y2="1"><stop offset="0" stop-color="#8fa58a"/><stop offset=".45" stop-color="#6f8a58"/><stop offset="1" stop-color="#5f7a3e"/></linearGradient></defs>
    <polygon points="248,0 427,0 427,186 226,186" fill="url(#gA)"/>
  </svg>
  <h2 class="abs head-font sec-title" style="left:39px;top:431px"><span class="teal">Our Innovative</span><br>Technology</h2>
  <p class="abs body-copy" style="left:39px;top:470px;width:176px">At Vlm Quarvex, our comprehensive technological solutions help the industry to become more sustainable and efficient with the spendings. We will balance qualitative training experience for soldiers and security forces with real life experiences and a real life feel.</p>
  <p class="abs body-copy" style="left:39px;top:516px;width:176px">Our platform will have a wide range of features created with the aim to help the industry become more aware of their environmental footprint. In order to empower our users to do better,</p>
  <span class="abs pill" style="left:40px;top:550px;width:60px;height:15px;font-size:4.8px">Learn More <i></i></span>

  <div class="abs clients" style="top:592px;height:121px"></div>
  <h2 class="abs head-font clients-title" style="left:114px;top:612px">What Our Clients Have To Say</h2>
  <span class="abs chev" style="left:42px;top:651px;transform:rotate(45deg)"></span>
  <span class="abs chev" style="left:377px;top:651px;transform:rotate(-135deg)"></span>
  <div class="abs avatar" style="left:66px;top:630px" role="img" aria-label="Client portrait"></div>
  <span class="abs quote-mark" style="left:100px;top:632px">“</span>
  <p class="abs quote-text" style="left:114px;top:638px">Lorem ipsum dolor sit amet, consectetur adipiscing elit, sed do eiusmod tempor incididunt ut labore et dolore magna aliqua. Ut enim ad minim veniam, quis nostrud exercitation ullamco laboris nisi ut aliquip ex ea commodo consequat.</p>
  <span class="abs quote-mark" style="left:212px;top:663px">”</span>
  <p class="abs client-name" style="left:114px;top:675px;color:#fff">John Doe</p>
  <p class="abs client-co" style="left:114px;top:683px;color:#fff">Company Name</p>

  <h2 class="abs head-font contact-title" style="top:744px">Contact <span class="teal">Us</span></h2>
  <p class="abs col-title" style="left:40px;top:777px">Contact Details</p>
  <svg class="abs icon" style="left:40px;top:800px" viewBox="0 0 10 10"><path d="M5 0a3.5 3.5 0 0 0-3.5 3.5C1.5 6 5 10 5 10s3.5-4 3.5-6.5A3.5 3.5 0 0 0 5 0zm0 5a1.4 1.4 0 1 1 0-2.8A1.4 1.4 0 0 1 5 5z" fill="#00a79d"/></svg>
  <p class="abs small-copy" style="left:51px;top:799px;width:120px">Lindqvist Vej 18, 4100 Nordby, Denmark</p>
  <div class="abs map" style="left:40px;top:818px;width:139px;height:55px" role="img" aria-label="Dark street map showing the office location"></div>
  <svg class="abs icon" style="left:40px;top:881px" viewBox="0 0 10 10"><path d="M2 0.5l2 2-1 1.5c.6 1.3 1.7 2.4 3 3l1.5-1 2 2-1.3 1.5C4.5 9.5 0.5 5.5 0.5 1.8z" fill="#00a79d"/></svg>
  <p class="abs small-copy" style="left:49px;top:880px">+45 20114873</p>
  <svg class="abs icon" style="left:40px;top:891px" viewBox="0 0 10 10"><rect x="0.5" y="2" width="9" height="6.5" fill="#00a79d"/><path d="M0.5 2l4.5 3.5L9.5 2" stroke="#fff" stroke-width=".8" fill="none"/></svg>
  <p class="abs small-copy" style="left:49px;top:890px">info@vlmquarvex.com</p>

  <p class="abs col-title" style="left:200px;top:777px">Get In Touch</p>
  <div class="abs field" style="left:200px;top:798px;width:88px;height:16px">Name</div>
  <div class="abs field" style="left:300px;top:798px;width:87px;height:16px">Phone Number</div>
  <div class="abs field" style="left:200px;top:819px;width:88px;height:16px">Email Address</div>
  <div class="abs field" style="left:300px;top:819px;width:87px;height:16px">Subject</div>
  <div class="abs field tall" style="left:200px;top:839px;width:187px;height:31px">Messagge</div>
  <span class="abs submit" style="left:200px;top:884px;width:41px;height:15px">SUBMIT</span>

  <footer class="abs bar-footer" style="top:927px">
    <span class="abs" style="left:40px;top:6px">© 2021 Vlm Quarvex &nbsp;| &nbsp;Terms and Conditions &nbsp;| &nbsp;Privacy</span>
    <span class="abs ring" style="left:355px;top:4.5px"></span>
    <span class="abs ring" style="left:367px;top:4.5px"></span>
    <span class="abs ring" style="left:379px;top:4.5px"></span>
  </footer>
</section>

<!-- ============ PAGE B ============ -->
<section class="page page-b">
  <header class="abs site-header">
    <div class="abs brand" style="left:40px;top:11px"><span class="brand-dot"></span>VLM QUARVEX</div>
    <span class="abs nav-link active" style="left:148px">Home</span>
    <span class="abs nav-link" style="left:174px">Who We Are</span>
    <span class="abs nav-link" style="left:215px">Services</span>
    <span class="abs nav-link" style="left:247px">Our Technology</span>
    <span class="abs nav-link" style="left:296px">Contact Us</span>
    <span class="abs quote-btn">Get A Quote</span>
  </header>

  <svg class="abs" style="left:0;top:0" width="427" height="280" role="img" aria-label="Instructor guiding a kneeling shooter at a snowy outdoor range">
    <defs><linearGradient id="gB" x1="0" y1="0" x2="1" y2="1"><stop offset="0" stop-color="#a29a8d"/><stop offset=".5" stop-color="#8c8478"/><stop offset="1" stop-color="#5b5a55"/></linearGradient></defs>
    <polygon fill="url(#gB)" points="0,32 427,32 427,238 416,239 386,241 343,250 312,247 284,255 248,257 215,271 184,258 147,255 119,246 87,250 48,243 16,240 0,236"/>
    <g fill="#fff" stroke="#00a79d" stroke-width="1.5">
      <circle cx="16" cy="240" r="2.2"/><circle cx="48" cy="243" r="2.2"/><circle cx="87" cy="250" r="2.2"/><circle cx="119" cy="246" r="2.2"/><circle cx="147" cy="255" r="2.2"/><circle cx="184" cy="258" r="2.2"/><circle cx="215" cy="271" r="2.2"/><circle cx="248" cy="257" r="2.2"/><circle cx="284" cy="255" r="2.2"/><circle cx="312" cy="247" r="2.2"/><circle cx="343" cy="250" r="2.2"/><circle cx="386" cy="241" r="2.2"/><circle cx="416" cy="239" r="2.2"/>
    </g>
  </svg>
  <div class="abs brand" style="left:35px;top:104px;font-size:20px;gap:6px"><span class="brand-dot" style="width:12px;height:12px"></span>VLM QUARVEX</div>
  <p class="abs hero-copy" style="left:35px;top:142px">Welcome to Vlm Quarvex, the advanced Technology Company paving the way to the future.</p>
  <span class="abs pill" style="left:36px;top:169px;width:68px;height:18px">Learn More <i></i></span>

  <div class="abs" style="left:40px;top:298px;width:144px;height:144px;border-radius:50%;border:3px solid var(--teal);background:linear-gradient(135deg,#8e8a7f,#5e5b52)" role="img" aria-label="Armed tactical team in helmets aiming on a range"></div>
  <h2 class="abs head-font sec-title" style="left:210px;top:303px"><span class="teal">Our Innovative</span><br>Technology</h2>
  <p class="abs body-copy" style="left:210px;top:341px;width:176px">At Vlm Quarvex, our comprehensive technological solutions help the industry to become more sustainable and efficient with the spendings. We will balance qualitative training experience for soldiers and security forces with real life experiences and a real life feel.</p>
  <p class="abs body-copy" style="left:210px;top:381px;width:176px">Our platform will have a wide range of features created with the aim to help the industry become more aware of their environmental footprint. In order to empower our users to do better,</p>
  <span class="abs pill" style="left:210px;top:420px;width:60px;height:15px;font-size:4.8px">Learn More <i></i></span>

  <div class="abs soft-band" style="left:0;top:470px;width:427px;height:142px"></div>
  <svg class="abs" style="left:0;top:470px" width="427" height="142" role="img" aria-label="Group of armed tactical operators walking across a dirt range">
    <defs><linearGradient id="gC" x1="0" y1="0" x2="0" y2="1"><stop offset="0" stop-color="#a9a49a"/><stop offset=".6" stop-color="#7e7a70"/><stop offset="1" stop-color="#b7ab96"/></linearGradient></defs>
    <polygon points="232,0 427,0 427,142 203,142" fill="url(#gC)"/>
  </svg>
  <h2 class="abs head-font sec-title" style="left:39px;top:497px">Who <span class="teal">We Are</span></h2>
  <p class="abs sec-sub" style="left:39px;top:520px">We develop an add on for TK40 rifles.</p>
  <p class="abs body-copy" style="left:39px;top:531px;width:160px;line-height:8.6px">Vlm Quarvex is a leading provider of cutting-edge technologies and services, offering scalable solutions for the defense and security industry of all sizes. Founded by a group of friends who started by scribbling their ideas on a bus ride in San Francisco. Today we are working on innovative solutions to disrupt the training industry with a sustainable solution.</p>

  <div class="abs clients" style="top:612px;height:122px"></div>
  <h2 class="abs head-font clients-title" style="left:114px;top:633px">What Our Clients Have To Say</h2>
  <span class="abs chev" style="left:42px;top:672px;transform:rotate(45deg)"></span>
  <span class="abs chev" style="left:377px;top:672px;transform:rotate(-135deg)"></span>
  <div class="abs avatar" style="left:66px;top:651px" role="img" aria-label="Client portrait"></div>
  <span class="abs quote-mark" style="left:100px;top:653px">“</span>
  <p class="abs quote-text" style="left:114px;top:659px">Lorem ipsum dolor sit amet, consectetur adipiscing elit, sed do eiusmod tempor incididunt ut labore et dolore magna aliqua. Ut enim ad minim veniam, quis nostrud exercitation ullamco laboris nisi ut aliquip ex ea commodo consequat.</p>
  <span class="abs quote-mark" style="left:212px;top:684px">”</span>
  <p class="abs client-name" style="left:114px;top:696px;color:#fff">John Doe</p>
  <p class="abs client-co" style="left:114px;top:704px;color:#fff">Company Name</p>

  <h2 class="abs head-font contact-title" style="top:765px">Contact <span class="teal">Us</span></h2>
  <p class="abs col-title" style="left:40px;top:798px">Contact Details</p>
  <svg class="abs icon" style="left:40px;top:821px" viewBox="0 0 10 10"><path d="M5 0a3.5 3.5 0 0 0-3.5 3.5C1.5 6 5 10 5 10s3.5-4 3.5-6.5A3.5 3.5 0 0 0 5 0zm0 5a1.4 1.4 0 1 1 0-2.8A1.4 1.4 0 0 1 5 5z" fill="#00a79d"/></svg>
  <p class="abs small-copy" style="left:51px;top:820px;width:120px">Lindqvist Vej 18, 4100 Nordby, Denmark</p>
  <div class="abs map" style="left:40px;top:839px;width:139px;height:55px" role="img" aria-label="Dark street map showing the office location"></div>
  <svg class="abs icon" style="left:40px;top:902px" viewBox="0 0 10 10"><path d="M2 0.5l2 2-1 1.5c.6 1.3 1.7 2.4 3 3l1.5-1 2 2-1.3 1.5C4.5 9.5 0.5 5.5 0.5 1.8z" fill="#00a79d"/></svg>
  <p class="abs small-copy" style="left:49px;top:901px">+45 20114873</p>
  <svg class="abs icon" style="left:40px;top:912px" viewBox="0 0 10 10"><rect x="0.5" y="2" width="9" height="6.5" fill="#00a79d"/><path d="M0.5 2l4.5 3.5L9.5 2" stroke="#fff" stroke-width=".8" fill="none"/></svg>
  <p class="abs small-copy" style="left:49px;top:911px">info@vlmquarvex.com</p>

  <p class="abs col-title" style="left:200px;top:798px">Get In Touch</p>
  <div class="abs field" style="left:200px;top:819px;width:88px;height:16px">Name</div>
  <div class="abs field" style="left:300px;top:819px;width:87px;height:16px">Phone Number</div>
  <div class="abs field" style="left:200px;top:840px;width:88px;height:16px">Email Address</div>
  <div class="abs field" style="left:300px;top:840px;width:87px;height:16px">Subject</div>
  <div class="abs field tall" style="left:200px;top:860px;width:187px;height:31px">Messagge</div>
  <span class="abs submit" style="left:200px;top:905px;width:41px;height:15px">SUBMIT</span>

  <footer class="abs full-footer">
    <div class="abs brand" style="left:49px;top:26px;font-size:12px;color:var(--teal);gap:4px"><span class="brand-dot" style="width:8px;height:8px"></span>VLM QUARVEX</div>
    <span class="abs ring" style="left:67px;top:66px"></span>
    <span class="abs ring" style="left:79px;top:66px"></span>
    <span class="abs ring" style="left:91px;top:66px"></span>
    <span class="abs ring" style="left:103px;top:66px"></span>

    <p class="abs f-head" style="left:161px;top:24px">Quick Links</p>
    <p class="abs f-link" style="left:161px;top:37px">Home<br>Who We Are<br>Services<br>Our Technology<br>Contact Us</p>

    <p class="abs f-head" style="left:230px;top:24px">About Company</p>
    <p class="abs f-link" style="left:230px;top:37px">Terms &amp; Condition<br>Security Statement<br>Privacy Policy<br>FAQ<br>Refund Policy</p>

    <p class="abs f-head" style="left:304px;top:24px">Contact Us</p>
    <p class="abs f-label" style="left:312px;top:40px">Phone</p>
    <p class="abs f-val" style="left:312px;top:45px">+45 20114873</p>
    <p class="abs f-label" style="left:312px;top:58px">Email</p>
    <p class="abs f-val" style="left:312px;top:63px">info@vlmquarvex.com</p>
    <p class="abs f-label" style="left:312px;top:76px">Location</p>
    <p class="abs f-val" style="left:312px;top:81px;width:80px">Lindqvist Vej 18, 4100 Nordby, Denmark</p>

    <div class="abs" style="left:40px;top:104px;width:347px;height:1px;background:rgba(255,255,255,.18)"></div>
    <p class="abs" style="left:0;width:427px;text-align:center;top:113px;font-size:5px">2021 Copyright - VLM QUARVEX | All Rights Reserved</p>
    <span class="abs" style="left:395px;top:100px;width:11px;height:11px;border-radius:50%;background:var(--teal)"></span>
    <span class="abs" style="left:398.5px;top:104.5px;width:4px;height:4px;border-left:1px solid #fff;border-top:1px solid #fff;transform:rotate(45deg)"></span>
  </footer>
</section>

</body>
</html>
```